Lumen Cove Skincare - Package Design

New Beauty label needing product packaging design. Looking for elegant and stylish design to represent our premium brand.

This project is for 1 label and 1 box design. The winning designer will be assigned another project for the next product in the range. (to be paid as a new project)

This product is for "Dead Sea Mud Mask". Please see the label format and jar attached. Please note there are 2 different jars we are considering (will have a mud inside). Please feel free to choose whichever one suits your design best.

The labels and boxes are to retain the product information, such as size, ingredients etc, but is to be updated to our brand. You can move or display the other information as you wish.

the size of the dead sea mud mask color box is 72*72*85mm (length*width*height)
the size of dead sea mud mask label is 218*58mm (width*height)

Target Market(s)

Women 15 to 65

Requirements
Must have
• Must be elegant and represent our brand which is a premium beauty product.
Should not have
• Dark blue. Dark purple etc. Colours should compliment the logo

```html
<!DOCTYPE html>
<html lang="en">
<head>
<meta charset="utf-8">
<title>Lumen Cove Skincare – Dead Sea Mud Mask Packaging</title>
<link rel="stylesheet" href="https://fonts.googleapis.com/css2?family=Oswald:wght@400;600&display=swap">
<style>
  :root {
    --canvas: #ece9dc;
    --jet: #1d1a1a;
    --jet-soft: #2a2625;
    --lid-rim: #3a3635;
    --gold: #d4ac1e;
    --gold-light: #f3e25a;
    --gold-deep: #a9820f;
  }
  * { margin: 0; padding: 0; box-sizing: border-box; }
  html, body { width: 1200px; height: 1200px; overflow: hidden; }
  body {
    background: var(--canvas);
    font-family: "Oswald", sans-serif;
    position: relative;
  }

  /* Front label panel */
  .label {
    position: absolute;
    left: 170px; top: 60px;
    width: 860px; height: 570px;
    background: linear-gradient(160deg, var(--jet-soft), var(--jet) 60%);
    border-radius: 18px;
    overflow: hidden;
  }
  .label__arch {
    position: absolute;
    left: 320px; top: 60px;
    width: 220px; height: 190px;
    border-radius: 110px 110px 0 0;
    background: radial-gradient(circle at 45% 35%, var(--gold-light), var(--gold) 55%, var(--gold-deep));
    display: flex; flex-direction: column; align-items: center; justify-content: center;
    padding-top: 20px;
  }
  .label__brand {
    color: var(--jet);
    font-weight: 400;
    text-align: center;
    line-height: 1.1;
  }
  .label__brand-main { display: block; font-size: 30px; letter-spacing: 1px; }
  .label__brand-sub { display: block; font-size: 13px; letter-spacing: 6px; margin-top: 4px; }

  .label__title {
    position: absolute;
    left: 0; right: 0; top: 262px;
    text-align: center;
    color: var(--gold);
    font-weight: 600;
    font-size: 62px;
    line-height: 0.98;
    letter-spacing: 1px;
  }
  .label__claims {
    position: absolute;
    left: 0; right: 0; top: 395px;
    text-align: center;
    color: var(--gold);
    font-weight: 400;
    font-size: 14px;
    line-height: 1.5;
    letter-spacing: 0.5px;
  }
  .label__claims p + p { margin-top: 4px; }
  .label__claims .label__net { margin-top: 12px; }

  .label__band-line {
    position: absolute;
    left: 0; right: 0; bottom: 72px;
    height: 2px;
    background: var(--gold);
  }
  .label__band {
    position: absolute;
    left: 0; right: 0; bottom: 36px;
    height: 26px;
    background: linear-gradient(90deg, var(--gold-deep), var(--gold-light) 45%, var(--gold) 75%, var(--gold-deep));
  }

  /* Jar lid */
  .lid {
    position: absolute;
    left: 360px; top: 670px;
    width: 480px; height: 480px;
  }
  .lid svg { display: block; }
  .lid__brand {
    position: absolute;
    inset: 0;
    display: flex; flex-direction: column; align-items: center; justify-content: center;
    color: var(--gold);
    font-weight: 400;
    text-align: center;
  }
  .lid__brand-main { font-size: 54px; letter-spacing: 2px; line-height: 1; }
  .lid__brand-sub { font-size: 18px; letter-spacing: 10px; margin-top: 10px; padding-left: 10px; }
</style>
</head>
<body>

  <section class="label" aria-label="Dead Sea Mud Mask jar label">
    <div class="label__arch">
      <p class="label__brand">
        <span class="label__brand-main">Lumen Cove</span>
        <span class="label__brand-sub">SKINCARE</span>
      </p>
    </div>

    <h1 class="label__title">DEAD SEA<br>MUD MASK</h1>

    <div class="label__claims">
      <p>ANTI ACNE | DEEP SKIN CLEANSER | PORE REDUCER</p>
      <p>100% NATURAL MINERAL-INFUSED DETOXIFIER PACKED WITH VITAMINS TO PROMOTE YOUTHFUL SKIN</p>
      <p class="label__net">250G | 80FL.OZ</p>
    </div>

    <div class="label__band-line"></div>
    <div class="label__band"></div>
  </section>

  <section class="lid" aria-label="Jar lid">
    <svg width="480" height="480" viewBox="0 0 480 480">
      <defs>
        <linearGradient id="ringGold" x1="0" y1="0" x2="1" y2="1">
          <stop offset="0" stop-color="#f3e25a"/>
          <stop offset="0.5" stop-color="#d4ac1e"/>
          <stop offset="1" stop-color="#a9820f"/>
        </linearGradient>
      </defs>
      <circle cx="240" cy="240" r="238" fill="#3a3635"/>
      <circle cx="240" cy="240" r="228" fill="#1d1a1a"/>
      <circle cx="240" cy="240" r="150" fill="none" stroke="url(#ringGold)" stroke-width="3"/>
    </svg>
    <p class="lid__brand">
      <span class="lid__brand-main">Lumen Cove</span>
      <span class="lid__brand-sub">SKINCARE</span>
    </p>
  </section>

</body>
</html>
```